New label for vitamin and supplement products

We are a a Vitamin and Supplement company called Bright Harbor. We have been in business for 30 years and the branding needs a significant refresh.

We need all new packaging, including logo, colors, etc.

We want to have a fresh, clean, brand that inspires confidence and quality.

The website is Brightharbor.com and will also be updated.

Please ask any questions. Every idea is a good one.

```html
<!DOCTYPE html>
<html lang="en">
<head>
<meta charset="utf-8">
<title>Bright Harbor – Full Tide Minerals Label</title>
<link href="https://fonts.googleapis.com/css2?family=Montserrat:wght@900&family=Open+Sans:wght@400;600;700&display=swap" rel="stylesheet">
<style>
  :root {
    --backdrop: #eceef2;
    --label-white: #ffffff;
    --accent-pink: #f0c8e6;
    --tab-pink: #f2c6e8;
    --ink: #1b1b1b;
    --brand-grey: #5a5a5a;
    --band-black: #151515;
    --tab-text: #ffffff;
  }
  * { margin: 0; padding: 0; box-sizing: border-box; }
  html, body {
    width: 1200px;
    height: 1200px;
    overflow: hidden;
    background: var(--backdrop);
  }
  .label {
    position: absolute;
    left: 180px;
    top: 60px;
    width: 840px;
    height: 1080px;
    background: var(--label-white);
    overflow: hidden;
    font-family: "Open Sans", Arial, sans-serif;
  }
  .brand-name {
    position: absolute;
    top: 105px;
    left: 0;
    width: 840px;
    text-align: center;
    font-family: "Open Sans", Arial, sans-serif;
    font-weight: 600;
    font-size: 66px;
    line-height: 80px;
    color: var(--brand-grey);
  }
  .title-band {
    position: absolute;
    left: 0;
    top: 265px;
    width: 770px;
    height: 356px;
    background: var(--accent-pink);
  }
  .product-title {
    position: absolute;
    left: 122px;
    top: 330px;
    font-family: "Montserrat", Arial, sans-serif;
    font-weight: 900;
    font-size: 98px;
    line-height: 124px;
    color: var(--ink);
    letter-spacing: -1px;
    white-space: nowrap;
  }
  .title-marker {
    position: absolute;
    left: 582px;
    top: 621px;
    width: 50px;
    height: 41px;
    background: var(--ink);
  }
  .tagline {
    position: absolute;
    left: 122px;
    top: 676px;
    font-size: 46px;
    line-height: 64px;
    color: var(--ink);
  }
  .supplement-type {
    position: absolute;
    left: 122px;
    top: 818px;
    font-size: 46px;
    line-height: 71px;
    color: var(--ink);
  }
  .count-tab {
    position: absolute;
    left: 517px;
    top: 805px;
    width: 161px;
    height: 190px;
    background: var(--tab-pink);
    border-radius: 18px 18px 0 0;
    text-align: center;
    color: var(--tab-text);
  }
  .count-number {
    display: block;
    margin-top: 14px;
    font-weight: 700;
    font-size: 56px;
    line-height: 66px;
  }
  .count-unit {
    display: block;
    font-size: 36px;
    line-height: 46px;
  }
  .base-band {
    position: absolute;
    left: 0;
    top: 990px;
    width: 840px;
    height: 90px;
    background: var(--band-black);
  }
</style>
</head>
<body>
  <main class="label">
    <div class="brand-name">Bright Harbor</div>
    <div class="title-band"></div>
    <h1 class="product-title">FULL TIDE<br>MINERALS</h1>
    <div class="title-marker"></div>
    <p class="tagline">17 vital minerals</p>
    <p class="supplement-type">Dietary<br>Supplement</p>
    <div class="count-tab">
      <span class="count-number">60</span>
      <span class="count-unit">Caplets</span>
    </div>
    <div class="base-band"></div>
  </main>
</body>
</html>
```